Web Design Project For Hot Tub Company [DETAILED instructions inside with a VIDEO!!]

Site will be aimed at individual consumers and not business owners. The purpose of the site is NOT to sell hot tubs online, but to entice people to come to the actual store.

According to the client, it is mostly MEN who initiate contact, while the WOMEN come into the store. This means, the design elements should appeal to MEN more so than to WOMEN.

Right now, the clients only web presence is this Brindle Listings ad:

-LINK-
http://www.brindlelistings.example/albuquerque-nm/mip/spa-shop-albuquerque-813274605
-

Site layout will include an area for a large video on the top, below the menu bar. There will be NO optin form on this site, so there will be some open space next to the video. Be creative and use it to highlight something unique about the business (they pride themselves on their high-end products, low monthly maintenance fees, and after purchase care-the company offers FREE delivery, installation, training, 2 free "drain and fills" and a 30-exchange guarantee.) with an interesting graphic.

Below that, a standard FOUR column layout with images and text that can be hyperlinked later to interior pages. Interior pages will include a sidebar. Below that, a standard footer.

Navigation will include the following: Home, About Us, Models, After Market Service, Testimonials, , and Contact Us.

Ideally, this company's site should appeal to higher income couples without children, new homeowners, and wealthy families.

Company's Logo is attached

Target Market(s)

Upper middle class to upper class families-boyfriends, husbands and fathers mostly.

Industry/Entity Type

Business

Requirements
Must have
• -Area for a video player
-Fun, inviting layout that will appeal to upper middle class husbands and boyfriends.
Nice to have
• *Creativity!!!!

A website with a header, a horizontal navigation bar, a video, a four column layout, and a footer are pretty common and standard. Use your creativity to stay within our parameters without looking like a boring, cookie-cutter website.

Though the site should appeal to men, do not exclude women.
Should not have
• *An optin form

```html
<!DOCTYPE html>
<html lang="en">
<head>
<meta charset="utf-8">
<title>Crestwater Spas – Home</title>
<link href="https://fonts.googleapis.com/css2?family=PT+Sans:ital,wght@0,400;0,700;1,700&family=Fira+Sans:wght@400;500&family=Arimo:wght@400;700&family=Alfa+Slab+One&display=swap" rel="stylesheet">
<style>
:root{
  --brand-blue:#0e7fa6;
  --brand-blue-light:#1fb2dc;
  --panel-teal:#0f6f8c;
  --heading-dark:#333;
  --text-dark:#3a3a3a;
  --nav-grey:#e6e6e6;
  --promo-yellow:#c9c51a;
  --button-olive:#9ea51a;
  --ribbon-pink:#c2335b;
  --footer-bg:#2b2b2b;
  --footer-text:#e0e0e0;
  --page-bg:#f7f8f9;
}
*{box-sizing:border-box;margin:0;padding:0}
html,body{width:1200px;height:940px;overflow:hidden}
body{position:relative;background:linear-gradient(180deg,#fff 0%,var(--page-bg) 40%,#fff 70%);font-family:"PT Sans",sans-serif;color:var(--text-dark)}
.top-rule{position:absolute;left:0;top:0;width:1200px;height:4px;background:var(--brand-blue)}
.brand{position:absolute;left:118px;top:48px;display:flex;align-items:center;gap:10px;font-family:"PT Sans",sans-serif;font-weight:700;font-size:30px;color:var(--brand-blue);white-space:nowrap}
.brand-dot{width:22px;height:22px;border-radius:50%;background:var(--brand-blue-light)}
.main-nav a{position:absolute;top:68px;height:32px;border-radius:16px;background:linear-gradient(#fafafa,var(--nav-grey));box-shadow:0 2px 3px rgba(0,0,0,.2);font-size:13px;color:#222;text-decoration:none;display:flex;align-items:center;justify-content:center;white-space:nowrap}
.main-nav a::after{content:"";position:absolute;bottom:-14px;left:50%;width:34px;height:5px;margin-left:-17px;border-radius:50%;background:rgba(0,0,0,.15)}
.main-nav a.active{background:linear-gradient(#35c3ea,var(--brand-blue));color:#fff}
.person-cutout{position:absolute;left:0;top:140px;width:170px;height:330px;border-radius:60px 60px 20px 20px;background:linear-gradient(#8fa9cf,#b9c4cf 60%,#c9c9c9)}
.video-frame{position:absolute;left:120px;top:148px;width:625px;height:347px;border-radius:22px 22px 10px 10px;background:linear-gradient(#2a2a2a,#111 85%,#c9cbcd 85%,#9a9da0)}
.video-screen{position:absolute;left:48px;top:22px;width:530px;height:268px;background:linear-gradient(#4aa6d8 0%,#5cb8e2 15%,#6fae3e 30%,#3f8b22 100%)}
.play-button{position:absolute;left:226px;top:96px;width:74px;height:74px;border-radius:50%;background:#3a3a3a;border:4px solid #ddd}
.play-button::after{content:"";position:absolute;left:27px;top:17px;border-left:26px solid #fff;border-top:16px solid transparent;border-bottom:16px solid transparent}
.player-bar{position:absolute;left:0;bottom:0;width:530px;height:28px;background:rgba(20,20,20,.75);display:flex;align-items:center;gap:8px;padding:0 8px;font-family:Arimo,sans-serif;font-size:10px;color:#ddd}
.player-bar .btn{width:12px;height:12px;border:1px solid #bbb}
.player-bar .track{width:160px;height:3px;background:#888;position:relative;margin-left:6px}
.player-bar .track::after{content:"";position:absolute;left:80px;top:-3px;width:8px;height:9px;background:#ddd}
.player-bar .time{margin-left:auto}
.promo{position:absolute;left:783px;top:143px;width:303px;height:340px;background:#fff;box-shadow:0 2px 6px rgba(0,0,0,.2);overflow:hidden}
.promo-head{position:absolute;left:4px;top:5px;width:293px;height:88px;border-top:6px solid var(--panel-teal);border-bottom:4px solid #6d7a1b;display:flex;align-items:center;padding-left:30px}
.promo-head .brand{position:static;font-size:24px}
.ribbon{position:absolute;left:162px;top:30px;width:170px;height:24px;background:var(--ribbon-pink);transform:rotate(35deg);color:#fff;font-family:Arimo,sans-serif;font-weight:700;font-size:12px;text-align:center;line-height:24px;white-space:nowrap}
.promo-body{position:absolute;left:4px;top:93px;width:293px;height:243px;background:var(--panel-teal)}
.promo-photo{position:absolute;right:0;top:0;width:170px;height:243px;border-radius:60px 0 0 0;background:linear-gradient(#b7cfdb,#8a7560 70%,#c9ad5d)}
.promo-free{position:absolute;left:11px;top:8px;font-family:"Alfa Slab One",serif;font-size:36px;color:var(--promo-yellow)}
.promo-title{position:absolute;left:10px;top:50px;font-family:Arimo,sans-serif;font-size:27px;color:#fff}
.promo-text{position:absolute;left:13px;top:91px;width:104px;font-family:Arimo,sans-serif;font-size:12.5px;line-height:18px;color:#fff}
.promo-button{position:absolute;left:12px;top:193px;width:111px;height:28px;border-radius:14px;background:linear-gradient(#c4cc2a,var(--button-olive));color:#fff;font-family:Arimo,sans-serif;font-weight:700;font-size:13px;text-align:center;line-height:28px}
.feature{position:absolute;top:537px;width:225px;height:263px;border:2px solid #eee;border-radius:6px;background:linear-gradient(#fff,#e2e2e2);box-shadow:0 8px 6px -6px rgba(0,0,0,.2)}
.feature h2{position:absolute;left:14px;top:8px;font-family:"Fira Sans",sans-serif;font-weight:400;font-size:24px;color:var(--heading-dark);white-space:nowrap}
.feature h2 span{color:var(--brand-blue);font-weight:500}
.feature-photo{position:absolute;left:12px;top:55px;width:199px;height:95px;border:4px solid #fff;box-shadow:0 0 2px rgba(0,0,0,.2)}
.feature p{position:absolute;left:10px;top:158px;width:203px;font-size:12px;line-height:16px;text-align:justify;letter-spacing:.3px}
.feature p em{font-weight:700}
.more-button{position:absolute;left:52px;top:240px;width:117px;height:31px;border-radius:4px;background:linear-gradient(#30b3e0,var(--brand-blue));color:#fff;font-family:Arimo,sans-serif;font-weight:700;font-size:13px;text-align:center;line-height:31px;text-decoration:none}
.site-footer{position:absolute;left:0;top:847px;width:1200px;height:93px;background:var(--footer-bg);font-family:Arimo,sans-serif;font-size:12px;color:var(--footer-text)}
.footer-nav{position:absolute;left:118px;top:35px;letter-spacing:.5px;white-space:nowrap}
.footer-nav span{margin:0 11px}
.copyright{position:absolute;left:118px;top:59px;letter-spacing:.5px}
.site-footer .brand{left:auto;right:110px;top:28px;color:#9a9a9a}
.site-footer .brand-dot{background:#9a9a9a}
</style>
</head>
<body>
<div class="top-rule"></div>

<header>
  <div class="brand"><span class="brand-dot"></span>Crestwater Spas</div>
  <nav class="main-nav">
    <a class="active" style="left:486px;width:84px">Home</a>
    <a style="left:579px;width:83px">About Us</a>
    <a style="left:673px;width:84px">Models</a>
    <a style="left:763px;width:135px">After Market Service</a>
    <a style="left:911px;width:87px">Testimonials</a>
    <a style="left:1013px;width:84px">Contact Us</a>
  </nav>
</header>

<div class="person-cutout" role="img" aria-label="Smiling man in a blue sweater presenting the video"></div>

<section class="video-frame">
  <div class="video-screen" role="img" aria-label="Video still of a happy couple playing on a green meadow">
    <div class="play-button"></div>
    <div class="player-bar">
      <span class="btn"></span><span class="btn"></span>
      <span class="track"></span>
      <span class="time">00:38/01:29</span>
    </div>
  </div>
</section>

<aside class="promo">
  <div class="promo-head"><div class="brand"><span class="brand-dot"></span>Crestwater Spas</div></div>
  <div class="ribbon">REGISTER NOW!</div>
  <div class="promo-body">
    <div class="promo-photo" role="img" aria-label="Family with two small children outdoors"></div>
    <div class="promo-free">FREE</div>
    <div class="promo-title">Delivery</div>
    <div class="promo-text">Ipsum has been the industry's standard dummy text ever since the 1500s</div>
    <div class="promo-button">Learn More</div>
  </div>
</aside>

<main>
  <article class="feature" style="left:116px">
    <h2>About <span>Business</span></h2>
    <div class="feature-photo" role="img" aria-label="Group of friends standing by a pool in front of a house" style="background:linear-gradient(#b8c6b0,#8a9a7a 55%,#4f86b6)"></div>
    <p><em>Vestibulum rutrum pharetra diam, eget dapibus leo</em> vehicula ut. Fusce aliquam, odio eget adipiscing diam, eget dapibus leo vehicula....</p>
    <a class="more-button">More Details</a>
  </article>
  <article class="feature" style="left:367px">
    <h2>About <span>Models</span></h2>
    <div class="feature-photo" role="img" aria-label="Woman in white in front of green foliage" style="background:linear-gradient(#2f5a22,#4f7d33 50%,#2c4d1c)"></div>
    <p><em>Vestibulum rutrum pharetra diam, eget dapibus leo</em> vehicula ut. Fusce aliquam, odio eget adipiscing diam, eget dapibus leo vehicula....</p>
    <a class="more-button">More Details</a>
  </article>
  <article class="feature" style="left:619px">
    <h2>Market <span>Services</span></h2>
    <div class="feature-photo" role="img" aria-label="Couple toasting with drinks in a pool" style="background:linear-gradient(#3fc2e8,#9fd7e6 50%,#2ba9d6)"></div>
    <p><em>Vestibulum rutrum pharetra diam, eget dapibus leo</em> vehicula ut. Fusce aliquam, odio eget adipiscing diam, eget dapibus leo vehicula....</p>
    <a class="more-button">More Details</a>
  </article>
  <article class="feature" style="left:867px">
    <h2>Who We <span>Are</span></h2>
    <div class="feature-photo" role="img" aria-label="Group of friends standing by a pool in front of a house" style="background:linear-gradient(#b8c6b0,#8a9a7a 55%,#4f86b6)"></div>
    <p><em>Vestibulum rutrum pharetra diam, eget dapibus leo</em> vehicula ut. Fusce aliquam, odio eget adipiscing diam, eget dapibus leo vehicula....</p>
    <a class="more-button">More Details</a>
  </article>
</main>

<footer class="site-footer">
  <div class="footer-nav">Home<span>~</span>About Us<span>~</span>Models<span>~</span>After Market Service<span>~</span>Testimonials<span>~</span>Contact Us</div>
  <div class="copyright">Copyright &nbsp;&nbsp; 2013, Privacy Policy</div>
  <div class="brand"><span class="brand-dot"></span>Crestwater Spas</div>
</footer>
</body>
</html>
```